Sanora-Velantis Flyer Patient Day

We need a flyer for an event (format A5, double-sided, portrait format). This event is aimed at lymphology patients. The aim of this case is to inform patients about the progress of treatment, to show trends and to get in touch with them. The structure of the Flyer must be follows: - Page 1: with the title and date and logo of Sanora-Velantis - Page 2: with info text and details of the event The text templates are attached below: (180216_VA_Briefing_Workshopflyer_Betroffenentag_Sanora-Velantis.docx) The logos for the partners are also attached below. The following design inputs: 1) Please visit the following website: www.sanora-velantis.ch and use the logo of Sanora-Velantis 2) The visual language should be appropriate for the theme of networking (No Go people, preferably using graphical elements. ) Please use elements of the lymphology pathways, 3) For texts please use the following font: Roboto-Light For running text please use the following font: PT-Serif-Italic, sans-serif 4) The texts must be reader-friendly Please note that this flyer is not for Brevido, but for Sanora-Velantis.

```html
<!DOCTYPE html>
<html lang="de">
<head>
<meta charset="utf-8">
<title>Sanora-Velantis – Betroffenentag Flyer</title>
<link href="https://fonts.googleapis.com/css2?family=Roboto:wght@300;400;500;700&display=swap" rel="stylesheet">
<style>
  :root {
    --bg: #e4e4e4;
    --paper: #ffffff;
    --band: #f0f0f0;
    --ink: #2e2e2e;
    --title: #6d6d6f;
    --label: #e5333f;
    --magenta: #d8338a;
    --orange: #f0901e;
    --blue: #3bb6e8;
    --green: #009a76;
    --lime: #b5d334;
    --path: #cfcfcf;
  }
  * { box-sizing: border-box; margin: 0; padding: 0; }
  html, body { width: 1200px; height: 1200px; overflow: hidden; }
  body { background: var(--bg); font-family: "Roboto", Arial, sans-serif; font-weight: 300; color: var(--ink); position: relative; }

  .page { position: absolute; top: 215px; width: 540px; height: 770px; background: var(--paper); overflow: hidden; box-shadow: 0 4px 18px rgba(0,0,0,.12); }
  .page--back { left: 40px; }
  .page--front { left: 620px; }

  .pathway { position: absolute; display: block; }
  .pathway__line { fill: none; stroke: var(--path); stroke-width: 1.5; }
  .node--magenta { fill: var(--magenta); }
  .node--orange { fill: var(--orange); }
  .node--blue { fill: var(--blue); }
  .node--green { fill: var(--green); }
  .node--lime { fill: var(--lime); }

  .brand { position: absolute; display: flex; align-items: center; gap: 10px; font-weight: 400; color: var(--ink); }
  .brand__mark { border-radius: 50%; background: var(--green); flex: none; }

  /* back page */
  .top-band { position: absolute; left: 0; top: 0; width: 100%; height: 210px; background: var(--band); }
  .page--back .brand { left: 40px; top: 96px; font-size: 16px; }
  .page--back .brand__mark { width: 14px; height: 14px; }
  .intro { position: absolute; left: 185px; top: 88px; width: 320px; font-size: 14px; line-height: 20px; }

  .details { position: absolute; top: 243px; font-size: 11.5px; line-height: 15.5px; }
  .details--left { left: 46px; width: 225px; }
  .details--right { left: 279px; width: 250px; }
  .details h3 { color: var(--label); font-weight: 400; font-size: 12.5px; letter-spacing: .3px; margin-bottom: 1px; }
  .details section { margin-bottom: 14px; }
  .details strong { font-weight: 500; }
  .details ul { list-style: none; }
  .details li { padding-left: 15px; position: relative; }
  .details li::before { content: "•"; position: absolute; left: 0; }
  .details li.sub { padding-left: 34px; }
  .details li.sub::before { left: 26px; }

  .rule { position: absolute; height: 1px; background: #d3d3d3; }
  .page--back .rule { left: 142px; right: 0; top: 516px; }

  .register { position: absolute; left: 220px; width: 250px; top: 556px; text-align: center; }
  .register__lead { font-size: 12px; }
  .register__mail { font-size: 16px; font-weight: 500; margin: 5px 0 7px; }
  .register__deadline { font-size: 10px; }

  .partners { position: absolute; left: 0; bottom: 0; width: 100%; height: 125px; background: var(--band); }
  .partners h4 { text-align: center; font-weight: 400; font-size: 11.5px; letter-spacing: 1px; margin-top: 26px; }
  .partners__row { display: flex; justify-content: space-around; align-items: center; margin-top: 26px; padding: 0 20px; font-size: 15px; font-weight: 500; color: #555; }

  /* front page */
  .page--front .brand { left: 0; right: 0; top: 170px; justify-content: center; font-size: 30px; }
  .page--front .brand__mark { width: 28px; height: 28px; }
  .event-title { position: absolute; left: 30px; right: 30px; top: 400px; text-align: center; font-size: 44px; line-height: 58px; color: var(--title); font-weight: 300; }
  .event-date { position: absolute; left: 0; right: 0; top: 598px; text-align: center; color: var(--green); font-size: 17px; font-weight: 700; letter-spacing: .5px; }
  .page--front .rule { left: 55px; right: 75px; top: 660px; }
  .orgs { position: absolute; left: 0; right: 0; top: 688px; display: flex; justify-content: space-around; padding: 0 40px; font-size: 11.5px; color: #444; }
</style>
</head>
<body>

<article class="page page--back">
  <div class="top-band"></div>
  <svg class="pathway" style="left:0;top:0" width="540" height="70" viewBox="0 0 540 70" aria-hidden="true">
    <path class="pathway__line" d="M0 52 C90 20 160 58 250 34 S420 10 540 40"/>
    <circle class="node--green" cx="62" cy="37" r="6"/>
    <circle class="node--magenta" cx="178" cy="46" r="5"/>
    <circle class="node--blue" cx="300" cy="25" r="7"/>
    <circle class="node--orange" cx="415" cy="22" r="5"/>
    <circle class="node--lime" cx="500" cy="31" r="6"/>
  </svg>
  <div class="brand"><span class="brand__mark"></span>Sanora-Velantis</div>
  <p class="intro">Die Stiftung Sanora-Velantis organisiert mit den beiden Betroffenenorganisationen Verein Lipoalpina und Lymphverbund Schweiz die folgende Tagung:</p>

  <div class="details details--left">
    <section><h3>DATUM</h3><p>16. Juni 2018</p></section>
    <section><h3>ZEIT</h3><p><strong>ab 9h00</strong> Eintreffen der Besucher (Industrieausstellung geöffnet)<br><strong>ab 10h00</strong> Start des Tagungsprogramms</p></section>
    <section><h3>ORT</h3><p>TBD, Aarau</p></section>
    <section><h3>ZIELGRUPPE</h3><p>Betroffene und Angehörige</p></section>
  </div>

  <div class="details details--right">
    <section><h3>PROGRAMME</h3>
      <ul>
        <li>Darstellung Lip- und Lymphödem</li>
        <li>Vorstellung der Organisationen</li>
        <li class="sub">Stiftung Sanora-Velantis</li>
        <li class="sub">Verein Lipoalpina</li>
        <li class="sub">Lymphverbund Schweiz</li>
        <li>Ausgewogene Ernährung</li>
        <li>Mode für Betroffene</li>
        <li>Sport als Bestandteil der Therapie</li>
      </ul>
    </section>
    <section><h3>EINTRITT</h3><p>Teilnahmegebühren inkl. Mittagessen<br><strong>50.- pro Person,<br>jede weitere Person CHF 15.-</strong></p></section>
  </div>

  <svg class="pathway" style="left:0;top:490px" width="142" height="150" viewBox="0 0 142 150" aria-hidden="true">
    <path class="pathway__line" d="M0 20 C40 20 60 60 70 90 S110 140 142 26"/>
    <circle class="node--blue" cx="24" cy="21" r="5"/>
    <circle class="node--magenta" cx="66" cy="78" r="6"/>
    <circle class="node--lime" cx="100" cy="120" r="5"/>
    <circle class="node--orange" cx="136" cy="50" r="4"/>
  </svg>

  <div class="rule"></div>
  <div class="register">
    <p class="register__lead">Anmeldungen und Fragen via E-mail</p>
    <p class="register__mail">info@sanora-velantis.ch</p>
    <p class="register__deadline">Anmeldefrist : 20 Mai 2018</p>
  </div>

  <footer class="partners">
    <h4>PARTENAIRES</h4>
    <div class="partners__row"><span>Norvel medical</span><span>Brevido</span><span>Kastra</span><span>Sivoma</span></div>
  </footer>
</article>

<article class="page page--front">
  <svg class="pathway" style="left:0;top:0" width="540" height="130" viewBox="0 0 540 130" aria-hidden="true">
    <path class="pathway__line" d="M0 90 C100 40 180 110 270 70 S440 20 540 60"/>
    <path class="pathway__line" d="M270 70 C300 40 320 20 340 0"/>
    <circle class="node--lime" cx="70" cy="68" r="7"/>
    <circle class="node--magenta" cx="185" cy="88" r="6"/>
    <circle class="node--green" cx="270" cy="70" r="8"/>
    <circle class="node--blue" cx="395" cy="40" r="7"/>
    <circle class="node--orange" cx="490" cy="45" r="6"/>
    <circle class="node--blue" cx="322" cy="22" r="4"/>
  </svg>

  <div class="brand"><span class="brand__mark"></span>Sanora-Velantis</div>

  <h1 class="event-title">Betroffenen- und Angehörigentag Lip- und Lymphödem</h1>
  <p class="event-date">21 AVRIL 2018</p>
  <div class="rule"></div>
  <div class="orgs"><span>Verein Lipoalpina</span><span>Lymphverbund Schweiz</span></div>

  <svg class="pathway" style="left:0;top:720px" width="540" height="50" viewBox="0 0 540 50" aria-hidden="true">
    <path class="pathway__line" d="M0 38 C120 20 260 46 380 30 S500 22 540 26"/>
    <circle class="node--orange" cx="130" cy="27" r="5"/>
    <circle class="node--green" cx="300" cy="36" r="5"/>
    <circle class="node--magenta" cx="450" cy="26" r="5"/>
  </svg>
</article>

</body>
</html>
```